Business Card Design

We need two business cards - same design but with two different people's details.

We are a new start-up online cleaning business that allows people to book and pay for a quality home cleaner online.

We would like a professional yet overly formal style of business card.

Target Market(s)

18 - 65+ professionals

Industry/Entity Type

Business

Contact Information for Business Card

We would like two business cards but with the same design, the details are below:

Mark Pelletta
Director and Co-Founder
ph: 0491 352 807
Suite 4C, Level 3
517 Larkfield Road
Brindale NSW 2093
mark@tidvane.com.au

_______________________________________________________

Evadne Pelletta
Director and Co-Founder
ph: 0427 915364
Suite 4C, Level 3
517 Larkfield Road
Brindale NSW 2093
evadne@tidvane.com.au

Requirements
Must have
• although our style guide refers to orange and red, please stick to the blue/black/grey that is in the style guide.

also on the back of the card we would like the logo with our tag line which is on page 12 of the style guide.
Should not have
• no pictures of mops, cleaners etc

```html
<!DOCTYPE html>
<html lang="en">
<head>
<meta charset="utf-8">
<title>Tidvane Business Cards</title>
<link rel="stylesheet" href="https://fonts.googleapis.com/css2?family=Open+Sans:wght@400;600;700&display=swap">
<style>
  :root {
    --page: #ffffff;
    --ink: #000000;
    --charcoal: #333333;
    --brand-blue: #12a5df;
    --white: #ffffff;
    --tagline-light: #d6d6d6;
    --rule: #1b4f66;
    --bubble-light: #f4f7f9;
  }
  * { box-sizing: border-box; margin: 0; padding: 0; }
  html, body { width: 1200px; height: 1000px; overflow: hidden; background: var(--page); }
  body { position: relative; font-family: "Open Sans", Arial, sans-serif; }

  .card {
    position: absolute; top: 259px; width: 260px; height: 424px;
    border-radius: 22px; overflow: hidden;
    box-shadow: 2px 3px 5px rgba(0,0,0,0.35);
  }
  .card--back { background: var(--ink); }
  .card--front { background: var(--brand-blue); }
  .card-1 { left: 53px; }
  .card-2 { left: 330px; }
  .card-3 { left: 609px; }
  .card-4 { left: 887px; }

  /* Brand lockup */
  .brand-row { position: absolute; display: flex; align-items: center; gap: 8px; }
  .brand-dot { width: 40px; height: 40px; border-radius: 50%; flex: none; }
  .brand-name { font-weight: 700; line-height: 1; }
  .brand-tagline { font-size: 7px; color: var(--tagline-light); position: absolute; white-space: nowrap; }

  .card--back .brand-row { left: 50px; top: 48px; }
  .card--back .brand-dot { border: 3px solid var(--white); }
  .card--back .brand-name { color: var(--white); font-size: 22px; }
  .card--back .brand-tagline { left: 100px; top: 82px; }

  .bubbles { position: absolute; left: 0; right: 0; bottom: 0; }
  .card--back .bubbles {
    height: 264px;
    background: radial-gradient(ellipse at 55% 65%, #e9eef1 0%, #9a9fa3 45%, #000000 80%);
  }
  .card--front .bubbles {
    height: 110px;
    background: linear-gradient(to bottom, rgba(255,255,255,0) 0%, rgba(255,255,255,0.55) 70%, var(--bubble-light) 100%);
  }

  /* Front face */
  .logo-band {
    position: absolute; left: 0; right: 0; top: 53px; height: 120px;
    background: var(--white);
    display: flex; flex-direction: column; align-items: center; justify-content: center; gap: 10px;
  }
  .logo-band .brand-dot { width: 58px; height: 58px; border: 5px solid var(--brand-blue); }
  .logo-band .brand-name { color: var(--charcoal); font-size: 28px; }

  .person { position: absolute; left: 28px; top: 220px; width: 204px; }
  .person-name { font-size: 18px; color: var(--ink); font-weight: 400; text-transform: uppercase; letter-spacing: -0.2px; }
  .person-name strong { font-weight: 700; }
  .person-title { font-size: 10px; color: var(--ink); margin-left: 2px; padding-bottom: 6px; border-bottom: 1px solid var(--rule); }

  .contacts { list-style: none; margin-top: 22px; font-size: 8.5px; color: var(--ink); }
  .contacts li { display: flex; align-items: flex-start; gap: 9px; line-height: 15px; }
  .contacts svg { width: 8px; height: 8px; margin-top: 3.5px; flex: none; }
  .contacts .phone { font-weight: 700; }
  .contacts .indent { padding-left: 17px; }

  /* Standalone lockup */
  .lockup { position: absolute; left: 836px; top: 838px; display: flex; align-items: center; gap: 12px; }
  .lockup .brand-dot { width: 72px; height: 72px; border: 7px solid var(--brand-blue); }
  .lockup .brand-name { color: var(--charcoal); font-size: 38px; }
  .lockup-tagline { position: absolute; left: 84px; top: 54px; font-size: 11px; color: var(--charcoal); white-space: nowrap; }
</style>
</head>
<body>

  <section class="card card--back card-1">
    <div class="brand-row"><span class="brand-dot"></span><span class="brand-name">Tidvane</span></div>
    <p class="brand-tagline">Less fuss. Reserve a trusted cleaner today</p>
    <div class="bubbles" role="img" aria-label="Decorative pattern of white soap bubbles"></div>
  </section>

  <section class="card card--front card-2">
    <div class="logo-band"><span class="brand-dot"></span><span class="brand-name">Tidvane</span></div>
    <div class="person">
      <h2 class="person-name"><strong>Evadne</strong> Pelletta</h2>
      <p class="person-title">Director and Co-Founder</p>
      <ul class="contacts">
        <li><svg viewBox="0 0 10 10"><path d="M1 3 Q5 0 9 3 L8 4.5 L6.5 4 L6.5 3 Q5 2.5 3.5 3 L3.5 4 L2 4.5 Z M2.5 5 H7.5 L8.5 9 H1.5 Z" fill="currentColor"/></svg><span class="phone">0427 915364</span></li>
        <li><svg viewBox="0 0 10 10"><rect x="0.5" y="2" width="9" height="6.5" fill="currentColor"/><path d="M0.5 2 L5 5.5 L9.5 2" stroke="#12a5df" stroke-width="0.9" fill="none"/></svg><span>evadne@tidvane.com.au</span></li>
        <li><svg viewBox="0 0 10 10"><path d="M5 0.5 A3.3 3.3 0 0 1 8.3 3.8 C8.3 6 5 9.5 5 9.5 C5 9.5 1.7 6 1.7 3.8 A3.3 3.3 0 0 1 5 0.5 Z" fill="currentColor"/><circle cx="5" cy="3.8" r="1.2" fill="#12a5df"/></svg><span>Suite 4C, Level 3 517 Larkfield Road</span></li>
        <li class="indent">Brindale NSW 2093</li>
      </ul>
    </div>
    <div class="bubbles" role="img" aria-label="Decorative row of white soap bubbles along the bottom edge"></div>
  </section>

  <section class="card card--front card-3">
    <div class="logo-band"><span class="brand-dot"></span><span class="brand-name">Tidvane</span></div>
    <div class="person">
      <h2 class="person-name"><strong>Mark</strong> Pelletta</h2>
      <p class="person-title">Director and Co-Founder</p>
      <ul class="contacts">
        <li><svg viewBox="0 0 10 10"><path d="M1 3 Q5 0 9 3 L8 4.5 L6.5 4 L6.5 3 Q5 2.5 3.5 3 L3.5 4 L2 4.5 Z M2.5 5 H7.5 L8.5 9 H1.5 Z" fill="currentColor"/></svg><span class="phone">0491 352 807</span></li>
        <li><svg viewBox="0 0 10 10"><rect x="0.5" y="2" width="9" height="6.5" fill="currentColor"/><path d="M0.5 2 L5 5.5 L9.5 2" stroke="#12a5df" stroke-width="0.9" fill="none"/></svg><span>mark@tidvane.com.au</span></li>
        <li><svg viewBox="0 0 10 10"><path d="M5 0.5 A3.3 3.3 0 0 1 8.3 3.8 C8.3 6 5 9.5 5 9.5 C5 9.5 1.7 6 1.7 3.8 A3.3 3.3 0 0 1 5 0.5 Z" fill="currentColor"/><circle cx="5" cy="3.8" r="1.2" fill="#12a5df"/></svg><span>Suite 4C, Level 3 517 Larkfield Road</span></li>
        <li class="indent">Brindale NSW 2093</li>
      </ul>
    </div>
    <div class="bubbles" role="img" aria-label="Decorative row of white soap bubbles along the bottom edge"></div>
  </section>

  <section class="card card--back card-4">
    <div class="brand-row"><span class="brand-dot"></span><span class="brand-name">Tidvane</span></div>
    <p class="brand-tagline">Less fuss. Reserve a trusted cleaner today</p>
    <div class="bubbles" role="img" aria-label="Decorative pattern of white soap bubbles"></div>
  </section>

  <div class="lockup">
    <span class="brand-dot"></span><span class="brand-name">Tidvane</span>
    <p class="lockup-tagline">Less fuss. Reserve a trusted cleaner today</p>
  </div>

</body>
</html>
```